Northern Terrain Published Photographer Website

I need a website to feature a home page slide show of 6 of my top photos then a few simple pages including; gallery, bio, social, checkout, services
Updates

Need extra days to review

Target Market(s)

photography

Industry/Entity Type

Photographer

Coding

Coded - Design and coding required

Number of Pages Required

5+ page

Colors

Designer to choose colors to be used in the design.

Requirements
Must have
• clean eye catching elegant trendy
Nice to have
• unique and creative from other photographer websites

```html
<!DOCTYPE html>
<html lang="en">
<head>
<meta charset="utf-8">
<title>Elena Hartwell – Photographer</title>
<link rel="stylesheet" href="https://fonts.googleapis.com/css2?family=Noto+Serif:wght@700&family=Roboto:wght@400;500&display=swap">
<style>
  :root {
    --bg: #000000;
    --ink: #ffffff;
    --muted: #8a8a8a;
    --gold: #e6c64a;
    --icon-ink: #1a1a1a;
    --pink: #c8205e;
    --footer-bar: #1e1e1e;
    --line: #ffffff;
  }
  * { box-sizing: border-box; margin: 0; padding: 0; }
  html, body { width: 1200px; height: 3429px; overflow: hidden; background: var(--bg); }
  body { position: relative; font-family: "Roboto", Arial, sans-serif; color: var(--ink); }
  .abs { position: absolute; }

  /* Header */
  .site-header { left: 0; top: 0; width: 1200px; height: 82px; background: var(--bg); border-bottom: 1px solid #3a3a3a; }
  .brand { left: 91px; top: 28px; font-size: 22px; font-weight: 400; color: var(--ink); letter-spacing: 1px; }
  .main-nav a { position: absolute; top: 32px; font-size: 14px; color: var(--ink); text-decoration: none; }

  /* Hero */
  .hero { left: 0; top: 84px; width: 1200px; height: 465px;
    background:
      linear-gradient(180deg, rgba(0,0,0,0) 0%, rgba(0,0,0,0) 58%, rgba(20,10,0,0.55) 60%, rgba(0,0,0,0) 62%),
      linear-gradient(180deg, #2a1806 0%, #6a3e0c 18%, #c77a14 36%, #f4b02a 50%, #ffd266 54%, #d68a18 60%, #9a5a10 72%, #4a2a08 88%, #1e1204 100%); }
  .hero-brand { left: 114px; top: 462px; font-size: 34px; color: var(--ink); }

  /* About */
  .about-title { left: 23px; top: 571px; width: 576px; text-align: center;
    font-family: "Noto Serif", Georgia, serif; font-weight: 700; font-size: 29px; line-height: 1.28; }
  .rule { height: 3px; width: 60px; background: var(--line); }
  .about-text { left: 23px; top: 731px; width: 576px; text-align: center; color: var(--muted); font-size: 13px; line-height: 1.9; }
  .about-text p + p { margin-top: 18px; }
  .btn { display: flex; align-items: center; justify-content: center; border: 2px solid var(--ink);
    color: var(--ink); font-size: 13px; font-weight: 500; }
  .portrait { left: 651px; top: 601px; width: 499px; height: 665px;
    background: radial-gradient(ellipse 55% 45% at 58% 55%, #b8b2aa 0%, #d8cdb8 45%, #f6f6f6 75%), #f6f6f6; }

  /* Works */
  .section-title { left: 0; width: 1200px; text-align: center;
    font-family: "Noto Serif", Georgia, serif; font-weight: 700; font-size: 30px; }
  .photo { position: absolute; }

  /* Present band */
  .present { left: 0; top: 2457px; width: 1200px; height: 320px;
    background:
      radial-gradient(circle at 88% 78%, rgba(40,30,60,0.85) 0%, rgba(60,40,80,0.6) 16%, rgba(0,0,0,0) 24%),
      linear-gradient(180deg, #2e2646 0%, #4e3c6a 35%, #7a5a7e 55%, #c07a5a 72%, #8a5a5a 85%, #2a2030 100%); }
  .present-title { left: 0; top: 2530px; width: 1200px; text-align: center;
    font-family: "Noto Serif", Georgia, serif; font-weight: 700; font-size: 35px; line-height: 1.3; }
  .present-text { left: 0; top: 2652px; width: 1200px; text-align: center; font-size: 15px; }

  /* Social */
  .social-dot { width: 42px; height: 42px; border-radius: 50%; background: var(--gold);
    display: flex; align-items: center; justify-content: center; }
  .social-dot svg { width: 20px; height: 20px; }
  .strip-tile { position: absolute; top: 2857px; width: 240px; height: 240px; }
  .strip-arrow { top: 2962px; width: 16px; height: 30px; }
  .follow-btn { left: 485px; top: 3111px; width: 228px; height: 43px; background: var(--pink);
    display: flex; align-items: center; justify-content: center; font-size: 15px; }

  /* Footer */
  .footer-brand { left: 57px; top: 3222px; font-size: 38px; color: var(--ink); }
  .footer-heading { left: 649px; top: 3178px; font-family: "Noto Serif", Georgia, serif; font-weight: 700; font-size: 19px; }
  .footer-contact { left: 649px; top: 3226px; color: var(--gold); font-size: 13px; line-height: 1.6; }
  .footer-note { left: 649px; top: 3298px; width: 545px; font-size: 13px; line-height: 1.65; }
  .copyright { left: 0; top: 3394px; width: 1200px; height: 35px; background: var(--footer-bar);
    display: flex; align-items: center; justify-content: center; font-size: 11px; color: var(--muted); }
</style>
</head>
<body>

<header class="abs site-header">
  <div class="abs brand">Elena Hartwell</div>
  <nav class="main-nav">
    <a style="left:693px">Home</a>
    <a style="left:784px">Gallery</a>
    <a style="left:884px">Bio</a>
    <a style="left:958px">Checkout</a>
    <a style="left:1072px">Services</a>
  </nav>
</header>

<section>
  <div class="abs hero" role="img" aria-label="Sunset over calm water with silhouetted pier posts and a heron"></div>
  <div class="abs hero-brand">Elena Hartwell</div>
</section>

<section class="about">
  <h1 class="abs about-title">My Name is<br>Elena Hartwell,<br>I'm a photographer</h1>
  <div class="abs rule" style="left:281px;top:707px"></div>
  <div class="abs about-text">
    <p>Lorem ipsum dolor sit amet, consectetur adipiscing elit. Phasellus posuere nisl scelerisque lectus scelerisque tempus. Proin nec molestie turpis, eu luctus velit. Vestibulum ante ipsum primis in faucibus orci luctus et ultrices posuere cubilia Curae; Aenean fringilla ligula diam, at pulvinar quam maximus et.</p>
    <p>Cras eget urna dapibus, fermentum ligula cursus, dapibus nulla. Duis vel mattis nisl, eu interdum tortor. In eget mollis velit, vel lobortis felis. Donec scelerisque tellus ut nunc iaculis consequat. Aliquam bibendum mollis mi, eget fringilla neque consequat eget. Ut metus ligula, placerat et bibendum in, dictum a leo.</p>
  </div>
  <div class="abs btn" style="left:238px;top:990px;width:123px;height:43px">Read More</div>
  <div class="abs portrait" role="img" aria-label="Portrait of the photographer on a white backdrop"></div>
</section>

<section class="works">
  <h2 class="abs section-title" style="top:1362px">My Works</h2>
  <div class="abs rule" style="left:562px;top:1424px;width:78px"></div>

  <div class="photo" style="left:0;top:1451px;width:377px;height:336px;background:radial-gradient(circle at 62% 30%,#fff2e0 0%,#f0a0c0 10%,rgba(0,0,0,0) 30%),linear-gradient(180deg,#4a2470 0%,#b24a8a 35%,#e0607a 55%,#6a3080 75%,#1e1030 100%)" role="img" aria-label="Desert tree silhouetted against a purple sunset"></div>
  <div class="photo" style="left:0;top:1799px;width:377px;height:251px;background:linear-gradient(100deg,#5a7a2a 0%,#8aa04a 30%,#e8eef2 50%,#b89a5a 72%,#5a4a2a 100%)" role="img" aria-label="Waterfall below an arched bridge in autumn woods"></div>
  <div class="photo" style="left:0;top:2062px;width:377px;height:253px;background:radial-gradient(circle at 50% 25%,#fff4c0 0%,#f4c040 8%,rgba(0,0,0,0) 30%),linear-gradient(180deg,#3a2508 0%,#b87818 40%,#6a420c 62%,#1e1204 100%)" role="img" aria-label="Golden sunset over water with pier posts and a heron"></div>

  <div class="photo" style="left:393px;top:1451px;width:377px;height:254px;background:radial-gradient(ellipse 40% 30% at 50% 62%,#2e7a6a 0%,#3a6a5a 60%,rgba(0,0,0,0) 100%),linear-gradient(180deg,#e8e4dc 0%,#c8a478 18%,#a8582a 45%,#7a3a1a 80%,#5a2a14 100%)" role="img" aria-label="River bend curving through red canyon"></div>
  <div class="photo" style="left:393px;top:1719px;width:377px;height:267px;background:radial-gradient(circle at 55% 55%,#fff6e0 0%,#d8a070 14%,rgba(0,0,0,0) 24%),linear-gradient(180deg,#c0501a 0%,#e88a3a 22%,#f4c890 45%,#a85a2a 70%,#6a3018 100%)" role="img" aria-label="Glass sphere on red rock under a stone arch"></div>
  <div class="photo" style="left:393px;top:2000px;width:377px;height:251px;background:linear-gradient(180deg,#3a6ac0 0%,#a8c4e8 25%,#e8eef4 42%,#4a5a4a 55%,#8aa8d0 75%,#3a4a6a 100%)" role="img" aria-label="Snowy river reflecting a blue cloudy sky"></div>

  <div class="photo" style="left:789px;top:1451px;width:377px;height:304px;background:linear-gradient(180deg,#6a2414 0%,#c8401c 25%,#f07a28 45%,#f4b050 60%,#3a3a34 72%,#e4e8ee 88%,#b8bcc4 100%)" role="img" aria-label="Fiery clouds over a snowy forest canyon"></div>
  <div class="photo" style="left:789px;top:1769px;width:377px;height:304px;background:radial-gradient(circle at 60% 58%,#fff8d0 0%,#f0c060 6%,rgba(0,0,0,0) 18%),linear-gradient(180deg,#2050b0 0%,#5a8ad0 35%,#8a4a2a 50%,#d06a2a 58%,#6a3a24 75%,#3a2418 100%)" role="img" aria-label="Sunburst through a desert rock arch"></div>
  <div class="photo" style="left:789px;top:2085px;width:377px;height:253px;background:linear-gradient(180deg,#4a6a98 0%,#b8c8dc 30%,#8a8aa0 48%,#a87a5a 65%,#6a4a34 85%,#4a3424 100%)" role="img" aria-label="Grand canyon cliffs under cloudy sky"></div>

  <div class="abs btn" style="left:535px;top:2382px;width:128px;height:43px">Load More</div>
</section>

<section>
  <div class="abs present" role="img" aria-label="Blurred sunset shoreline with a glass sphere"></div>
  <h2 class="abs present-title">Present Works<br>Professionally</h2>
  <div class="abs rule" style="left:562px;top:2624px;width:78px"></div>
  <p class="abs present-text">Purchase our pictures and create beautiful collections of any size.</p>
  <div class="abs btn" style="left:523px;top:2706px;width:154px;height:44px">Purchase Now</div>
</section>

<section class="social">
  <div class="abs social-dot" style="left:493px;top:2793px" aria-label="Share">
    <svg viewBox="0 0 20 20"><path d="M4 14 L14 4 M8 4 H14 V10" fill="none" stroke="var(--icon-ink)" stroke-width="2.2" stroke-linecap="round" stroke-linejoin="round"/></svg>
  </div>
  <div class="abs social-dot" style="left:550px;top:2793px" aria-label="Like">
    <svg viewBox="0 0 20 20"><path d="M10 17 L3.5 10.5 A3.6 3.6 0 0 1 10 5.2 A3.6 3.6 0 0 1 16.5 10.5 Z" fill="var(--icon-ink)"/></svg>
  </div>
  <div class="abs social-dot" style="left:608px;top:2793px" aria-label="Message">
    <svg viewBox="0 0 20 20"><rect x="2.5" y="5" width="15" height="10.5" rx="1.5" fill="none" stroke="var(--icon-ink)" stroke-width="2"/><path d="M3 6 L10 11 L17 6" fill="none" stroke="var(--icon-ink)" stroke-width="2"/></svg>
  </div>
  <div class="abs social-dot" style="left:662px;top:2793px" aria-label="Location">
    <svg viewBox="0 0 20 20"><path d="M10 18 C6 13 4.5 10.5 4.5 8 A5.5 5.5 0 0 1 15.5 8 C15.5 10.5 14 13 10 18 Z" fill="var(--icon-ink)"/><circle cx="10" cy="8" r="2" fill="var(--gold)"/></svg>
  </div>

  <div class="strip-tile" style="left:0;background:linear-gradient(180deg,#7a848e 0%,#d8dce0 30%,#a8a49c 55%,#3a7282 72%,#6a5a4a 100%)" role="img" aria-label="Lake among canyon walls under clouds"></div>
  <div class="strip-tile" style="left:240px;background:radial-gradient(circle at 55% 58%,#fff8d0 0%,#f0c060 7%,rgba(0,0,0,0) 20%),linear-gradient(180deg,#2050b0 0%,#5a8ad0 40%,#c8602a 58%,#6a3a24 80%,#3a2418 100%)" role="img" aria-label="Sunburst through a rock arch"></div>
  <div class="strip-tile" style="left:480px;background:radial-gradient(circle at 50% 55%,#fff6e0 0%,#d8a070 14%,rgba(0,0,0,0) 26%),linear-gradient(180deg,#c0501a 0%,#f4c890 45%,#a85a2a 72%,#6a3018 100%)" role="img" aria-label="Glass sphere on red rock"></div>
  <div class="strip-tile" style="left:720px;background:linear-gradient(180deg,#6a2414 0%,#d04a1e 30%,#f0a040 55%,#3a3a34 68%,#e4e8ee 85%,#b8bcc4 100%)" role="img" aria-label="Fiery clouds over snowy forest"></div>
  <div class="strip-tile" style="left:960px;background:radial-gradient(ellipse 40% 30% at 50% 62%,#2e7a6a 0%,rgba(0,0,0,0) 100%),linear-gradient(180deg,#e8e4dc 0%,#c8a478 20%,#a8582a 45%,#5a2a14 100%)" role="img" aria-label="River bend in a red canyon"></div>

  <svg class="abs strip-arrow" style="left:6px" viewBox="0 0 16 30"><path d="M12 4 L4 15 L12 26" fill="none" stroke="#ffffff" stroke-width="2.5" stroke-linecap="round"/></svg>
  <svg class="abs strip-arrow" style="left:1178px" viewBox="0 0 16 30"><path d="M4 4 L12 15 L4 26" fill="none" stroke="#ffffff" stroke-width="2.5" stroke-linecap="round"/></svg>

  <div class="abs follow-btn">Follow Us on Snapline</div>
</section>

<footer>
  <div class="abs footer-brand">Elena Hartwell</div>
  <h3 class="abs footer-heading">My Location</h3>
  <div class="abs footer-contact">
    482 ALDER ROW, FERNBROOK, OREGON 97021<br>
    Phone : +1 55501234<br>
    E-Mail : info@elenahartwell.example
  </div>
  <p class="abs footer-note">Our studio space is located in downtown Fernbrook, right in the heart of the Willamette Valley, OR. Conveniently surrounded by some of the world's most talented craft producers. Come on by.</p>
  <div class="abs copyright">Copyright 2019</div>
</footer>

</body>
</html>
```